One page double sided catalog for fisheries

Create a double sided product catalog for a fresh yellowfin tuna exporting company in the Maldives called The Coral Wayfarers llc.
We export fresh yellowfin tuna caught from the wild using sustainable fishing methods to countries all across the globe. Our UPS are no MOQ requirements and Door Step Delivery. We aim to eliminate the middlemen in the business and deliver our products to our customer doorsteps in quantities that they can afford which will help them save money while getting the best fresh fish.
Main colors of our company are gold and blue to highlight premium quality while relating to the oceans
The catalog has to have 4-5 main point;
*Who we are
*What we do
*Our products
*About the Maldivian fisheries

The file attached is a draft we have received, but got disapproved as it doesn't have the catchy look and premium design elements we want to associate with our company and products.

Note: All text elements will be provided by us.

Industry/Entity Type

Business

Font styles to use
Serif
Sans Serif

Colors
0455a3

```html
<!DOCTYPE html>
<html lang="en">
<head>
<meta charset="utf-8">
<title>The Coral Wayfarers – Our Promise</title>
<link rel="stylesheet" href="https://fonts.googleapis.com/css2?family=Montserrat:wght@400;500;700&family=Source+Sans+3:ital,wght@0,400;0,600;1,400&display=swap">
<style>
  :root{
    --backdrop:#e6e7e9;
    --paper:#ffffff;
    --ocean-light:#2f86c4;
    --ocean-mid:#0d4f86;
    --ocean-deep:#0b2340;
    --night:#141b26;
    --gold:#e9962a;
    --band:rgba(60,62,68,.82);
    --ink:#2b2b2b;
    --muted:#555;
    --white:#ffffff;
    --soft-white:#dfe7ef;
    --salmon:#f07a55;
    --tuna-steel:#7c8c9a;
    --reef-pink:#d9538a;
  }
  *{box-sizing:border-box;margin:0;padding:0}
  html,body{width:984px;height:1200px;overflow:hidden;background:var(--backdrop)}
  body{font-family:"Source Sans 3",Arial,sans-serif;position:relative}
  .page{position:absolute;left:82px;top:20px;width:820px;height:1160px;background:var(--paper);overflow:hidden}

  .hero{position:absolute;left:0;top:0;width:820px;height:874px;
    background:
      radial-gradient(ellipse 70% 40% at 55% 28%, rgba(120,190,235,.55), transparent 70%),
      linear-gradient(180deg,#0e2d52 0,#154f85 160px,var(--ocean-light) 230px,var(--ocean-mid) 380px,var(--ocean-deep) 560px,var(--night) 874px)}
  .hero-rule{position:absolute;left:0;top:159px;width:820px;height:3px;background:var(--gold)}

  .brand{position:absolute;left:560px;top:118px;width:240px;text-align:right;
    font-family:"Montserrat",Arial,sans-serif;font-weight:500;font-size:19px;letter-spacing:.5px;color:var(--white)}

  .promise-title{position:absolute;left:42px;top:308px;font-family:"Montserrat",Arial,sans-serif;font-weight:700;font-size:41px;color:var(--white);letter-spacing:.5px}

  .pillar{position:absolute;top:366px;color:var(--white)}
  .pillar h2{font-family:"Montserrat",Arial,sans-serif;font-weight:500;font-size:17px;line-height:22px;margin-bottom:8px;text-transform:uppercase}
  .pillar p{font-size:12.4px;line-height:21.3px;color:var(--soft-white)}
  .pillar--freshness{left:42px;width:180px}
  .pillar--freshness p{text-align:justify}
  .pillar--quality{left:241px;width:165px}
  .pillar--moq{left:424px;width:168px}
  .pillar--delivery{left:611px;width:172px;top:342px}

  .sections{position:absolute;left:42px;top:688px;font-family:"Montserrat",Arial,sans-serif;font-size:17px;line-height:24px;color:var(--white)}

  .mission{position:absolute;left:0;top:755px;width:820px;height:119px;background:var(--band);
    text-align:center;color:var(--white);font-size:19px;line-height:24px;padding-top:13px}
  .mission strong{font-weight:600}
  .mission em{font-style:italic}
  .mission-rule{position:absolute;left:0;top:874px;width:820px;height:3px;background:var(--gold)}

  .product{position:absolute;top:884px;text-align:center}
  .product-art{margin:0 auto}
  .product h3{font-family:"Montserrat",Arial,sans-serif;font-weight:500;color:var(--ink);margin-top:12px;text-transform:uppercase}
  .product p{font-size:9.8px;line-height:12px;color:var(--muted);text-transform:uppercase;margin-top:2px}
  .product--loins{left:20px;width:230px}
  .product--loins .product-art{width:128px;height:96px;margin-top:14px;border-radius:40% 55% 45% 50%;background:linear-gradient(135deg,#f7a488,var(--salmon) 55%,#d9573a)}
  .product--loins h3{font-size:10.5px}
  .product--tuna{left:270px;width:290px}
  .product--tuna .product-art{width:270px;height:106px;border-radius:50% 40% 45% 50%/55% 50% 50% 45%;background:linear-gradient(180deg,#3f4f63,var(--tuna-steel) 45%,#e9edf0 70%,#ffffff)}
  .product--tuna h3{font-size:13px}
  .product--reef{left:585px;width:210px}
  .product--reef .product-art{width:136px;height:104px;border-radius:50%;background:linear-gradient(120deg,#f3c64a,var(--reef-pink) 45%,#7a5bc2)}
  .product--reef h3{font-size:13px}

  .footer-rule{position:absolute;left:35px;top:1106px;width:750px;height:1px;background:#f0c58a}
  .footer{position:absolute;left:0;top:1116px;width:820px;text-align:center;font-size:12.6px;color:var(--ink)}
</style>
</head>
<body>
<div class="page">
  <div class="hero" role="img" aria-label="Underwater photograph of a school of tuna swimming in deep blue ocean"></div>
  <div class="hero-rule"></div>

  <div class="brand">Coral Wayfarers</div>

  <h1 class="promise-title">OUR PROMISE</h1>

  <section class="pillar pillar--freshness">
    <h2>Freshness</h2>
    <p>Our fishermen deliver freshly caught fish, on a daily basis, that are kept in temperature controlled cabinets which are then transferred to our EU Certified packing factories. Our fish are processed on the same day and delivered overnight to our customers all across the globe, meaning they get “A” grade fresh yellowfin tuna less than 24 hours from their processed time. It doesn’t get any fresher than this.</p>
  </section>

  <section class="pillar pillar--quality">
    <h2>Quality</h2>
    <p>Our fish is processed and packed in an ISO and EU certified factory where stringent quality control practices are maintained. The factory is regularly audited for health, safety and quality features.</p>
  </section>

  <section class="pillar pillar--moq">
    <h2>Flexible MOQ</h2>
    <p>One of the greatest advantages of working with us is that we have absolutely no MOQ requirements for our customers. We serve according to our customer needs enabling them to have fresh stock throughout the year in volumes that they can afford to manage.</p>
  </section>

  <section class="pillar pillar--delivery">
    <h2>Door-Step<br>Delivery</h2>
    <p>We believe that, no matter where we are located, our customers deserve the best products and the best service, which is why we promise door step delivery to all our customers who require them. We partner with the best local courier agents to ensure our customer orders are delivered on a timely manner to their door steps, because we value your business and we believe every second counts.</p>
  </section>

  <div class="sections">
    <div>About Us</div>
    <div>Maldivian Fisheries</div>
  </div>

  <div class="mission">
    <div><strong>Vision and mission</strong> <em>statement of ours, include lorem ipsum</em></div>
    <div><strong>FRESH TUNA</strong> <em>exports from</em></div>
    <div><em>Maldives</em></div>
    <div><em>The Coral Wayfarers</em></div>
  </div>
  <div class="mission-rule"></div>

  <div class="product product--loins">
    <div class="product-art" role="img" aria-label="Photograph of a raw yellow fin tuna loin"></div>
    <h3>Yellow Fin Tuna Loins Loins &amp; Chunks</h3>
    <p>Are vacuumed packed, stored in styrofoam<br>boxes with gel ice 6kg, 15kg &amp; 25kg</p>
  </div>

  <div class="product product--tuna">
    <div class="product-art" role="img" aria-label="Illustration of a whole yellow fin tuna"></div>
    <h3>Yellow Fin Tuna</h3>
    <p>H&amp;G/G&amp;G headless gill &amp; gutted, packed in<br>cardboard boxes gross weight<br>90-95kg two per box</p>
  </div>

  <div class="product product--reef">
    <div class="product-art" role="img" aria-label="Illustration of a colourful reef fish"></div>
    <h3>Reef Fish</h3>
    <p>Customized order for specific species<br>of reef fish custom</p>
  </div>

  <div class="footer-rule"></div>
  <div class="footer">The Coral Wayfarers L.L.C | Seafood.Sourcing.Solutions | coralwayfarers.mv 771234 | 3345678</div>
</div>
</body>
</html>
```